Domestic Building Company requires professional webpage

We have an existing webpage that was never completed. We are a growing building company specialising in domestic building, renovations and commercial maintenance. We liaise closely with each of our clients to provide quality service they would be happy to recommend. Our easy approachable staff give our clients the confidence to discuss their needs and changes they may have along the way.
Our main source of new customers have been from recommendations of existing clients.
We would like our webpage to reflect our eye for detail and showcase our previous work.
The colour theme should be the same as the colours of our logo.
We would like the main page to really stand out with a slideshow of our pictures of works we have completed.
We would like the tabs to remain the same - Home, About Us, Our Services, Contact us.
In the Our Services section we would like each sub heading to be a link where viewers can see pictures from previous work we have completed.
Our current web page is www.kestrelbuilding.com.au

```html
<!DOCTYPE html>
<html lang="en">
<head>
<meta charset="utf-8">
<title>Kestrel Building Services – Services</title>
<link href="https://fonts.googleapis.com/css2?family=Roboto+Condensed:wght@400;700&family=Quattrocento:wght@400&family=Arimo:wght@400&display=swap" rel="stylesheet">
<style>
:root{
  --green:#8cc63f;
  --blue:#0066a1;
  --link:#1a1ad6;
  --body-text:#6b6b6b;
  --footer:#c9c9c9;
  --white:#ffffff;
  --dark:#333333;
}
*{box-sizing:border-box;margin:0;padding:0}
html,body{width:886px;height:1200px;overflow:hidden;background:var(--white)}
body{position:relative;font-family:"Roboto Condensed",sans-serif}
.top-bar{position:absolute;left:0;top:0;width:886px;height:7px;background:var(--green)}
.header-band{position:absolute;left:0;top:95px;width:886px;height:9px;background:var(--green)}
.member-badge{position:absolute;left:19px;top:28px;width:101px;height:52px;border:1px solid #9aaac4;background:#eef2f8}
.brand{position:absolute;left:300px;top:26px;display:flex;align-items:center;gap:12px}
.brand-name{font-family:"Roboto Condensed",sans-serif;font-weight:400;font-size:25px;color:var(--blue);line-height:1;white-space:nowrap}
.brand-mark{flex:none;width:40px;height:56px;background:var(--green)}
.phone{position:absolute;left:692px;top:38px;display:flex;align-items:center;gap:8px;font-family:"Arimo",sans-serif;font-size:16px;color:var(--dark);white-space:nowrap}
.search{position:absolute;left:654px;top:66px;width:206px;height:25px;border:1px solid #777;border-radius:8px;background:var(--white)}
.search svg{position:absolute;right:5px;top:3px}
.main-nav{position:absolute;left:0;top:104px;width:886px;height:46px}
.tab{position:absolute;top:0;height:44px;padding-top:9px;text-align:center;font-size:14px;font-weight:700;color:var(--dark);background:var(--green);clip-path:polygon(0 0,100% 0,100% 80%,0 100%);text-decoration:none}
.tab-home{left:244px;width:68px;padding-top:8px}
.tab-about{left:342px;width:68px;font-weight:400}
.tab-contact{left:577px;width:68px;font-weight:400}
.tab-active{left:431px;top:1px;width:126px;height:30px;padding-top:7px;background:var(--blue);color:var(--white);clip-path:none}
.service{position:absolute;width:352px}
.service-title{height:31px;background:var(--blue);border-bottom:3px solid var(--green);color:var(--white);font-weight:700;font-size:15.5px;text-align:center;line-height:28px;text-transform:uppercase;white-space:nowrap}
.service-title.left-aligned{text-align:left;padding-left:8px}
.service-body{display:flex;gap:11px;padding:12px 0 0 10px}
.photo{flex:none;width:129px;height:117px}
.service-text{font-family:"Quattrocento",serif;font-size:15.5px;line-height:28px;color:var(--body-text);white-space:nowrap}
.view-photos{position:absolute;right:0;font-size:12px;color:var(--link);text-decoration:none;white-space:nowrap}
.footer{position:absolute;left:0;top:1094px;width:886px;height:106px;background:var(--footer)}
.footer-nav{position:absolute;top:11px;left:0;width:886px;display:flex;justify-content:center;gap:20px;font-size:11px;color:var(--dark)}
.footer-nav .current{color:var(--link);display:flex;align-items:center;gap:5px}
.social{position:absolute;top:42px;left:0;width:886px;display:flex;justify-content:center;gap:20px}
.social span{width:22px;height:22px;border-radius:50%}
.copyright{position:absolute;top:94px;left:0;width:886px;text-align:center;font-size:8px;color:var(--dark)}
</style>
</head>
<body>
<div class="top-bar"></div>
<div class="member-badge"></div>
<div class="brand">
  <span class="brand-name">Kestrel Building Services</span>
  <span class="brand-mark"></span>
</div>
<div class="phone">
  <svg width="20" height="22" viewBox="0 0 20 22"><path d="M4 2h4l1 5-3 2c1 3 3 5 5 6l2-3 5 1v4c0 2-2 3-4 3C7 19 1 12 1 5c0-2 1-3 3-3z" fill="#222"/></svg>
  <span>0412 555 018</span>
</div>
<div class="search">
  <svg width="24" height="18" viewBox="0 0 24 18"><circle cx="9" cy="7" r="5.5" fill="none" stroke="#111" stroke-width="2"/><path d="M13 11l8 5" stroke="#111" stroke-width="3"/></svg>
</div>
<div class="header-band"></div>

<nav class="main-nav">
  <a class="tab tab-home">Home</a>
  <a class="tab tab-about">About Us</a>
  <a class="tab tab-active">SERVICES</a>
  <a class="tab tab-contact">Contact Us</a>
</nav>

<section class="service" style="left:45px;top:177px;height:200px">
  <h2 class="service-title left-aligned">Residential House Extensions and Renovations</h2>
  <div class="service-body">
    <div class="photo" role="img" aria-label="Photo of slatted timber screen extension" style="background:linear-gradient(135deg,#5a4a3c,#8a8478)"></div>
    <p class="service-text">Extend and /or add on to<br>your existing home to create<br>modern look to your exterior<br>and interior.</p>
  </div>
  <a class="view-photos" style="top:176px;right:11px">VIEW ALL PHOTOS</a>
</section>

<section class="service" style="left:483px;top:180px;height:200px">
  <h2 class="service-title">Pergolas</h2>
  <div class="service-body" style="padding-top:4px">
    <div class="photo" role="img" aria-label="Photo of covered timber pergola deck" style="background:linear-gradient(160deg,#6c7a6a,#7a4b33)"></div>
    <p class="service-text">Create a functional open air<br>outdoor room great for en-<br>tertaining, improve the ap-<br>pearance of home and add<br>extra space.</p>
  </div>
  <a class="view-photos" style="top:174px;right:14px">VIEW ALL PHOTOS</a>
</section>

<section class="service" style="left:47px;top:410px;height:200px">
  <h2 class="service-title">Decks</h2>
  <div class="service-body" style="padding-top:7px;padding-left:7px">
    <div class="photo" role="img" aria-label="Photo of timber gazebo deck in garden" style="background:linear-gradient(180deg,#9aa08c,#6b5a44 60%,#6f8a3e)"></div>
    <p class="service-text">We create and design various<br>shape and sized hardwood<br>decks to cater for all styles of<br>homes.</p>
  </div>
  <a class="view-photos" style="top:173px;right:0">VIEW ALL PHOTOS</a>
</section>

<section class="service" style="left:483px;top:409px;height:200px">
  <h2 class="service-title">Bathrooms</h2>
  <div class="service-body" style="padding-top:8px;padding-left:5px">
    <div class="photo" role="img" aria-label="Photo of modern bathroom vanity" style="background:linear-gradient(135deg,#d8dadc,#8e9296)"></div>
    <p class="service-text">Update and modernise exist-<br>ing or new bathrooms to suit<br>your style and needs.</p>
  </div>
  <a class="view-photos" style="top:176px;right:-8px">VIEW ALL PHOTOS</a>
</section>

<section class="service" style="left:47px;top:643px;height:200px">
  <h2 class="service-title">Commercial Fit-Out</h2>
  <div class="service-body" style="padding-top:7px">
    <div class="photo" role="img" aria-label="Photo of shop fit-out with glass doors" style="width:124px;background:linear-gradient(135deg,#4a3a30,#2a2a2a 60%,#7a7a72)"></div>
    <p class="service-text">Office or shop refurbishment<br>to create a practical and<br>modern design to cater for<br>your business.</p>
  </div>
  <a class="view-photos" style="top:170px;right:-2px">VIEW ALL PHOTOS</a>
</section>

<section class="service" style="left:483px;top:644px;height:200px">
  <h2 class="service-title">Timber Flooring</h2>
  <div class="service-body" style="padding-top:7px;padding-left:5px">
    <div class="photo" role="img" aria-label="Photo of dark timber deck flooring" style="background:linear-gradient(170deg,#6a7068,#3a2c24)"></div>
    <p class="service-text">We install all aspects of<br>timber flooring ranging from<br>floating floors through to<br>solid hardwood flooring for a<br>modern look.</p>
  </div>
  <a class="view-photos" style="top:175px;right:-8px">VIEW ALL PHOTOS</a>
</section>

<section class="service" style="left:46px;top:869px;height:210px">
  <h2 class="service-title">Aluminium / Timber</h2>
  <div class="service-body" style="padding-top:7px;padding-left:7px">
    <div class="photo" role="img" aria-label="Photo of living room with timber windows and doors" style="width:123px;height:118px;background:linear-gradient(135deg,#8a7a66,#c9c0b2 50%,#4a4038)"></div>
    <p class="service-text">We install a variety of timber<br>or aluminium windows and<br>doors including single doors,<br>bifold doors, sliding doors,<br>bifold windows, louvre and<br>sash windows.</p>
  </div>
  <a class="view-photos" style="top:202px;right:-1px">VIEW ALL PHOTOS</a>
</section>

<section class="service" style="left:483px;top:869px;height:210px">
  <h2 class="service-title">Building Maintenance</h2>
  <div class="service-body" style="padding-top:8px;padding-left:10px">
    <div class="photo" role="img" aria-label="Photo of repaired shed with teal door" style="height:121px;background:linear-gradient(90deg,#8a8c8a,#a8aaa6 60%,#6cc0b4)"></div>
    <p class="service-text">We provide a home repair<br>service for all internal and<br>external problems, no job too<br>small.</p>
  </div>
  <a class="view-photos" style="top:196px;right:-8px">VIEW ALL PHOTOS</a>
</section>

<footer class="footer">
  <nav class="footer-nav">
    <span>HOME</span>
    <span>ABOUT US</span>
    <span class="current"><svg width="14" height="10" viewBox="0 0 14 10"><path d="M1 1l4 4-4 4M7 1l4 4-4 4" fill="none" stroke="#1a1ad6" stroke-width="2"/></svg>SERVICES</span>
    <span>CONTACT US</span>
  </nav>
  <div class="social">
    <span style="background:#c84434"></span>
    <span style="background:#2a4f8f"></span>
    <span style="background:#b3251f"></span>
    <span style="background:#1f8fd0"></span>
    <span style="background:#c4242e"></span>
  </div>
  <p class="copyright">Copyright 2014 Kestrel Building Services Pty Ltd | ABN: 48 615 203 917 | Lic: 204816C</p>
</footer>
</body>
</html>
```